Tailbrook Website Design

Need a website for a Dog Grooiming business. Please make it simular to these:

https://www.furvanto.com
https://haulnorix.com
https://meadowpetrin.com
https://www.drivelumo.com/search/

```html
<!DOCTYPE html>
<html lang="en">
<head>
<meta charset="utf-8">
<title>Tailbrook – Careers</title>
<link href="https://fonts.googleapis.com/css2?family=Roboto:wght@400;500;700&family=Montserrat:wght@400;500&display=swap" rel="stylesheet">
<style>
  :root {
    --ink: #1c1c1c;
    --text: #444;
    --muted: #6a6a6a;
    --purple: #93309c;
    --footer: #262626;
    --white: #fff;
  }
  * { margin: 0; padding: 0; box-sizing: border-box; }
  html, body { width: 966px; height: 1200px; overflow: hidden; background: var(--white); }
  body { position: relative; font-family: "Roboto", sans-serif; color: var(--ink); }
  .abs { position: absolute; }

  .site-header { position: absolute; left: 0; top: 0; width: 966px; height: 87px; }
  .brand { left: 88px; top: 27px; font: 700 28px/1 "Roboto", sans-serif; color: var(--ink); }
  .contact-bar { right: 89px; top: 15px; display: flex; gap: 28px; font-size: 13px; align-items: center; }
  .contact-bar span { display: flex; align-items: center; gap: 6px; }
  .contact-bar b { font-size: 17px; font-weight: 500; }
  .main-nav { right: 89px; top: 54px; display: flex; gap: 24px; font-size: 13.5px; text-transform: uppercase; color: var(--text); }
  .main-nav .active { color: var(--purple); }

  .hero { left: 0; top: 87px; width: 966px; height: 366px; overflow: hidden; }
  .hero-photo { position: absolute; inset: 0; background: linear-gradient(90deg, #c9c9c9 0%, #d9dadb 35%, #b7a08c 60%, #2a2523 75%, #3a3431 100%); }
  .hero-curve { position: absolute; left: 0; bottom: 0; }
  .hero-title { left: 86px; top: 220px; font: 700 58px/1 "Roboto", sans-serif; color: var(--white); text-shadow: 0 2px 6px rgba(0,0,0,.35); }

  .intro-kicker { left: 0; width: 966px; top: 450px; text-align: center; font-size: 16px; color: var(--ink); }
  .intro-title { left: 0; width: 966px; top: 484px; text-align: center; font: 700 33px/1 "Roboto", sans-serif; }

  .perk { top: 569px; width: 250px; text-align: center; font-family: "Montserrat", sans-serif; }
  .perk-icon { height: 36px; display: flex; align-items: center; justify-content: center; }
  .perk h3 { margin-top: 30px; font-weight: 500; font-size: 18px; line-height: 22px; color: var(--text); }
  .perk p { margin-top: 11px; font-size: 12.5px; line-height: 21px; color: var(--muted); }

  .apply-btn { left: 405px; top: 752px; width: 157px; height: 49px; border-radius: 25px; background: var(--purple); color: var(--white); font: 700 17px/49px "Roboto", sans-serif; text-align: center; }

  .site-footer { left: 0; top: 858px; width: 966px; height: 342px; }
  .footer-brand { left: 88px; top: 978px; font: 700 32px/1 "Roboto", sans-serif; color: var(--white); }
  .footer-heading { top: 912px; font: 500 16px/1 "Roboto", sans-serif; color: var(--white); }
  .footer-links { top: 952px; list-style: none; font: 400 13px/23.5px "Montserrat", sans-serif; color: var(--white); }
  .footer-contact { left: 654px; top: 952px; font: 400 13px/23.5px "Montserrat", sans-serif; color: var(--white); }
  .footer-contact div { display: flex; gap: 7px; align-items: flex-start; }
  .footer-rule { left: 90px; top: 1119px; width: 786px; height: 1px; background: #555; }
  .copyright { left: 90px; top: 1147px; font: 400 12.5px/1 "Montserrat", sans-serif; color: var(--white); }
  .social { left: 760px; top: 1139px; display: flex; gap: 6px; }
  .social span { width: 35px; height: 35px; border: 1px solid var(--white); border-radius: 50%; }
</style>
</head>
<body>
<svg width="0" height="0" style="position:absolute">
  <defs>
    <linearGradient id="iconGrad" x1="0" y1="0" x2="1" y2="1">
      <stop offset="0" stop-color="#1ea0e6"/>
      <stop offset="1" stop-color="#9b2fa0"/>
    </linearGradient>
  </defs>
</svg>

<header class="site-header">
  <div class="abs brand">TAILBROOK</div>
  <div class="abs contact-bar">
    <span><svg width="12" height="12" viewBox="0 0 24 24"><path fill="#93309c" d="M6.6 10.8a15 15 0 0 0 6.6 6.6l2.2-2.2a1 1 0 0 1 1-.25 11 11 0 0 0 3.6.6 1 1 0 0 1 1 1V20a1 1 0 0 1-1 1A17 17 0 0 1 3 4a1 1 0 0 1 1-1h3.5a1 1 0 0 1 1 1 11 11 0 0 0 .6 3.6 1 1 0 0 1-.25 1z"/></svg>Call us <b>1 800 555 0142</b></span>
    <span><svg width="15" height="11" viewBox="0 0 24 18"><path fill="#93309c" d="M0 2v14a2 2 0 0 0 2 2h20a2 2 0 0 0 2-2V2L12 10z"/><path fill="#93309c" d="M1 0h22L12 8z"/></svg>Email us <b>info@tailbrook.com</b></span>
  </div>
  <nav class="abs main-nav">
    <span>Home</span><span>About</span><span>Locations</span><span class="active">Careers</span><span>Blog</span><span>Contact</span>
  </nav>
</header>

<section class="abs hero">
  <div class="hero-photo" role="img" aria-label="Groomer shampooing a black and tan dog in a bright salon"></div>
  <svg class="hero-curve" width="966" height="80" viewBox="0 0 966 80"><path d="M0 80 Q483 -46 966 80 Z" fill="#fff"/></svg>
</section>
<h1 class="abs hero-title">CAREERS</h1>

<p class="abs intro-kicker">Now Hiring Dog Groomers</p>
<h2 class="abs intro-title">GROOM YOUR BEST LIFE</h2>

<div class="abs perk" style="left:89px">
  <div class="perk-icon"><svg width="44" height="30" viewBox="0 0 44 30"><rect x="1.5" y="1.5" width="41" height="27" rx="1" fill="none" stroke="url(#iconGrad)" stroke-width="3"/><rect x="6" y="5" width="32" height="20" fill="url(#iconGrad)"/><ellipse cx="22" cy="15" rx="9" ry="10" fill="#fff"/><text x="22" y="20" text-anchor="middle" font-family="Roboto, sans-serif" font-weight="700" font-size="14" fill="#3a6fc9">1</text></svg></div>
  <h3>Make $6,000 /mo</h3>
  <p>Nemo enim ipsam voluptatem quia voluptas sit aspernatur aud</p>
</div>
<div class="abs perk" style="left:358px">
  <div class="perk-icon"><svg width="40" height="36" viewBox="0 0 40 36"><ellipse cx="5" cy="16" rx="4.5" ry="5.5" fill="url(#iconGrad)"/><ellipse cx="14" cy="6" rx="4.5" ry="5.5" fill="url(#iconGrad)"/><ellipse cx="26" cy="6" rx="4.5" ry="5.5" fill="url(#iconGrad)"/><ellipse cx="35" cy="16" rx="4.5" ry="5.5" fill="url(#iconGrad)"/><path d="M20 17c-6 0-12 9-12 14 0 5 6 4 12 2 6 2 12 3 12-2 0-5-6-14-12-14z" fill="url(#iconGrad)"/></svg></div>
  <h3>Celebrity Dogs</h3>
  <p>Nemo enim ipsam voluptatem quia voluptas sit aspernatur aud</p>
</div>
<div class="abs perk" style="left:634px">
  <div class="perk-icon"><svg width="30" height="36" viewBox="0 0 30 36"><circle cx="15" cy="9" r="8.5" fill="url(#iconGrad)"/><path d="M0 34c0-9 5-14 15-14s15 5 15 14a2 2 0 0 1-2 2H2a2 2 0 0 1-2-2z" fill="url(#iconGrad)"/></svg></div>
  <h3>In-house Concierge</h3>
  <p>Nemo enim ipsam voluptatem quia voluptas sit aspernatur aud</p>
</div>

<div class="abs apply-btn">APPLY NOW</div>

<svg class="abs site-footer" width="966" height="342" viewBox="0 0 966 342"><path d="M0 66 Q483 -66 966 66 V342 H0 Z" fill="#262626"/></svg>
<div class="abs footer-brand">TAILBROOK</div>
<h4 class="abs footer-heading" style="left:350px">QUICK LINKS</h4>
<ul class="abs footer-links" style="left:350px"><li>Home</li><li>About</li><li>Locations</li><li>Careers</li><li>Blog</li><li>Contact</li></ul>
<ul class="abs footer-links" style="left:470px"><li>Terms of Service</li><li>Privacy Policy</li><li>Book Online</li></ul>
<h4 class="abs footer-heading" style="left:654px">CONTACT US</h4>
<div class="abs footer-contact">
  <div><svg width="9" height="13" viewBox="0 0 10 14" style="margin-top:5px"><path fill="#fff" d="M5 0a5 5 0 0 0-5 5c0 4 5 9 5 9s5-5 5-9a5 5 0 0 0-5-5zm0 7a2 2 0 1 1 0-4 2 2 0 0 1 0 4z"/></svg><span>No 1 emo enim ipsam volupta<br>tem quia volupta</span></div>
  <div style="margin-top:23px"><svg width="11" height="11" viewBox="0 0 24 24" style="margin-top:6px"><path fill="#fff" d="M6.6 10.8a15 15 0 0 0 6.6 6.6l2.2-2.2a1 1 0 0 1 1-.25 11 11 0 0 0 3.6.6 1 1 0 0 1 1 1V20a1 1 0 0 1-1 1A17 17 0 0 1 3 4a1 1 0 0 1 1-1h3.5a1 1 0 0 1 1 1 11 11 0 0 0 .6 3.6 1 1 0 0 1-.25 1z"/></svg><span>1 800 555 0142</span></div>
  <div style="margin-top:23px"><svg width="14" height="11" viewBox="0 0 24 18" style="margin-top:6px"><path fill="#fff" d="M0 2v14a2 2 0 0 0 2 2h20a2 2 0 0 0 2-2V2L12 10z"/><path fill="#fff" d="M1 0h22L12 8z"/></svg><span>info@tailbrook.com</span></div>
</div>
<div class="abs footer-rule"></div>
<p class="abs copyright">© 2021, Tailbrook. All rights reserved.</p>
<div class="abs social"><span></span><span></span><span></span></div>
</body>
</html>
```